maple crest homeworks KOVA

Looking for business card design that represents our company. we are maple crest homeworks and we dedicate our skills of home energy efficiency to our customer by providing energy solution to their energy problems.
HVAC
SOLAR
INSULLATION
LIGHTING
DUCT TESTING
KOVA RATING.

```html
<!DOCTYPE html>
<html lang="en">
<head>
<meta charset="utf-8">
<title>Maple Crest Homeworks – Business Card</title>
<link rel="stylesheet" href="https://fonts.googleapis.com/css2?family=Arimo:wght@400;700&display=swap">
<style>
  :root {
    --stage: #2b2b2b;
    --card-black: #0b0b0b;
    --card-white: #f4f4f4;
    --green: #7cc242;
    --green-dark: #4f8a22;
    --green-glow: #8fd14f;
    --ink-light: #e8e8e8;
    --icon-grey: #cfcfcf;
  }
  * { box-sizing: border-box; margin: 0; padding: 0; }
  html, body { width: 1200px; height: 997px; overflow: hidden; }
  body {
    background: var(--stage);
    font-family: "Arimo", Arial, sans-serif;
    position: relative;
  }
  .card {
    position: absolute;
    top: 345px;
    width: 540px;
    height: 308px;
    border-radius: 22px;
    overflow: hidden;
  }
  .card--back { left: 40px; background: var(--card-black); }
  .card--front { left: 620px; background: var(--card-white); }

  /* Back side */
  .service-row {
    position: absolute;
    left: 40px; right: 40px;
    display: flex;
    justify-content: space-between;
    color: var(--green);
    font-size: 15px;
    letter-spacing: 1px;
  }
  .service-row--top { top: 58px; padding: 0 20px 6px; border-bottom: 2px solid var(--green); }
  .service-row--bottom { bottom: 58px; padding: 6px 20px 0; border-top: 2px solid var(--green); }
  .back-logo {
    position: absolute;
    left: 90px; right: 90px; top: 112px; height: 84px;
    border: 3px solid var(--green-glow);
    border-radius: 8px;
    box-shadow: 0 0 10px var(--green), inset 0 0 8px rgba(124,194,66,.5);
    display: flex; align-items: center; justify-content: center; gap: 12px;
  }

  /* Shared brand lockup */
  .brand-dot {
    width: 26px; height: 26px; border-radius: 50%;
    background: var(--green);
    flex: none;
  }
  .brand-name {
    color: var(--green);
    font-weight: 700;
    font-size: 22px;
    letter-spacing: 1px;
    text-transform: uppercase;
  }

  /* Front side */
  .front-shapes { position: absolute; inset: 0; }
  .front-logo {
    position: absolute;
    left: 120px; width: 300px; top: 42px; height: 80px;
    background: var(--card-black);
    border: 3px solid var(--green);
    border-radius: 8px;
    display: flex; align-items: center; justify-content: center; gap: 10px;
  }
  .front-logo .brand-name { font-size: 19px; }
  .person {
    position: absolute;
    left: 0; right: 0; top: 156px;
    text-align: center;
    color: var(--card-black);
  }
  .person__name { font-weight: 700; font-size: 17px; color: #fff; letter-spacing: 1px; text-transform: uppercase; }
  .person__title { font-size: 13px; margin-top: 2px; }
  .website {
    position: absolute;
    right: 26px; top: 210px;
    color: var(--green);
    font-weight: 700;
    font-size: 14px;
  }
  .contacts {
    position: absolute;
    left: 26px; top: 226px;
    list-style: none;
    color: var(--ink-light);
    font-size: 13px;
    line-height: 1.25;
  }
  .contacts li { display: flex; align-items: flex-start; gap: 10px; margin-bottom: 6px; }
  .contacts svg { width: 18px; height: 18px; flex: none; }
</style>
</head>
<body>

<section class="card card--back" aria-label="Business card back">
  <div class="service-row service-row--top">
    <span>HVAC</span><span>SOLAR</span><span>INSULLATION</span>
  </div>
  <div class="back-logo">
    <span class="brand-dot"></span>
    <span class="brand-name">Maple Crest Homeworks</span>
  </div>
  <div class="service-row service-row--bottom">
    <span>LIGHTING</span><span>DUCT TESTING</span><span>KOVA RATING</span>
  </div>
</section>

<section class="card card--front" aria-label="Business card front">
  <svg class="front-shapes" width="540" height="308" viewBox="0 0 540 308" aria-hidden="true">
    <rect x="0" y="200" width="540" height="108" fill="var(--card-black)"/>
    <polygon points="0,193 540,193 540,200 0,200" fill="var(--green)"/>
    <polygon points="110,200 150,150 470,150 540,150 540,160 490,160 440,200" fill="var(--green-dark)"/>
    <polygon points="90,200 140,150 430,150 480,200" fill="var(--green)"/>
  </svg>
  <div class="front-logo">
    <span class="brand-dot"></span>
    <span class="brand-name">Maple Crest Homeworks</span>
  </div>
  <div class="person">
    <p class="person__name">Marcus Delaney</p>
    <p class="person__title">Managing Director</p>
  </div>
  <p class="website">www.maplecresthw.com</p>
  <ul class="contacts">
    <li>
      <svg viewBox="0 0 18 18"><circle cx="9" cy="9" r="9" fill="var(--icon-grey)"/><path d="M5.5 6.5c0-1 1-1.5 1.5-1.5l1 2-1 1c.5 1.2 1.3 2 2.5 2.5l1-1 2 1c0 .5-.5 1.5-1.5 1.5-3 0-5.5-2.5-5.5-5.5z" fill="var(--card-black)"/></svg>
      <span>0491570156</span>
    </li>
    <li>
      <svg viewBox="0 0 18 18"><circle cx="9" cy="9" r="9" fill="var(--icon-grey)"/><rect x="4.5" y="6" width="9" height="6" fill="var(--card-black)"/><path d="M4.5 6l4.5 3.5L13.5 6" stroke="var(--icon-grey)" stroke-width="1" fill="none"/></svg>
      <span>info@maplecresthw.com</span>
    </li>
    <li>
      <svg viewBox="0 0 18 18"><circle cx="9" cy="9" r="9" fill="var(--icon-grey)"/><path d="M9 4a3.5 3.5 0 0 0-3.5 3.5C5.5 10 9 14 9 14s3.5-4 3.5-6.5A3.5 3.5 0 0 0 9 4z" fill="var(--card-black)"/><circle cx="9" cy="7.5" r="1.2" fill="var(--icon-grey)"/></svg>
      <span>PO Box 215 Ridgeview<br>B.C. QLD 4000</span>
    </li>
  </ul>
</section>

</body>
</html>
```